We are a music company that specializes in Music Mixing and Mastering. We also do vocal recording and create instrumentals for various artists. Our website is 738kv.com

Target Market(s)

Musicians, Record labels, rappers, and singers

Industry/Entity Type

Artists

Contact Information for Business Card

738KV
Industry Standard Mixing & Mastering
(555) 214-3907
sales@738kv.com
738kv.com

Requirements
Must have
• contact info and twitter (@738KV)

```html
<!DOCTYPE html>
<html lang="en">
<head>
<meta charset="utf-8">
<title>738KV Business Card</title>
<link href="https://fonts.googleapis.com/css2?family=Lato:wght@400;700;900&display=swap" rel="stylesheet">
<style>
  :root {
    --ink: #141414;
    --paper: #ffffff;
    --backdrop: #d9d9d9;
    --muted: #2a2a2a;
    --rule: #b5b5b5;
    --shadow: rgba(0, 0, 0, 0.22);
  }
  * { box-sizing: border-box; margin: 0; padding: 0; }
  html, body {
    width: 1200px;
    height: 926px;
    overflow: hidden;
    background: var(--backdrop);
    font-family: "Lato", Arial, sans-serif;
  }
  .sheet {
    width: 1200px;
    height: 926px;
    display: flex;
    flex-direction: column;
    align-items: center;
    justify-content: center;
    gap: 56px;
  }
  .card {
    width: 660px;
    height: 377px;
    position: relative;
    box-shadow: 0 10px 28px var(--shadow);
    overflow: hidden;
  }

  /* Back side */
  .card--back {
    background: var(--ink);
    color: var(--paper);
    display: flex;
    flex-direction: column;
    align-items: center;
    justify-content: center;
    gap: 18px;
  }
  .card--back .wordmark {
    font-size: 96px;
    font-weight: 900;
    letter-spacing: 2px;
    line-height: 1;
  }
  .card--back .tagline {
    font-size: 19px;
    font-weight: 700;
    letter-spacing: 1.2px;
    text-transform: uppercase;
  }

  /* Front side */
  .card--front {
    background: var(--paper);
    color: var(--ink);
  }
  .card--front .base-band {
    position: absolute;
    left: 0; right: 0; bottom: 0;
    height: 40px;
    background: var(--ink);
  }
  .card--front .content {
    position: absolute;
    left: 0; right: 0; top: 0; bottom: 40px;
    display: flex;
    align-items: center;
  }
  .card--front .brand {
    width: 48%;
    padding-left: 48px;
  }
  .card--front .wordmark {
    font-size: 68px;
    font-weight: 900;
    letter-spacing: 1px;
    line-height: 1;
  }
  .card--front .divider {
    width: 1px;
    height: 220px;
    background: var(--rule);
  }
  .card--front .details {
    padding-left: 30px;
  }
  .details .tagline {
    font-size: 20px;
    font-weight: 900;
    text-transform: uppercase;
    line-height: 1.2;
    letter-spacing: 0.6px;
    margin-bottom: 14px;
  }
  .contact-list { list-style: none; }
  .contact-list li {
    display: flex;
    align-items: center;
    gap: 10px;
    font-size: 19px;
    color: var(--muted);
    line-height: 1.5;
  }
  .contact-list svg {
    width: 16px;
    height: 16px;
    flex: none;
    fill: var(--ink);
  }
</style>
</head>
<body>
<main class="sheet">
  <section class="card card--back" aria-label="Card back">
    <div class="wordmark">738KV</div>
    <div class="tagline">Industry Standard Mixing &amp; Mastering</div>
  </section>

  <section class="card card--front" aria-label="Card front">
    <div class="content">
      <div class="brand">
        <div class="wordmark">738KV</div>
      </div>
      <div class="divider"></div>
      <div class="details">
        <p class="tagline">Industry Standard<br>Mixing &amp; Mastering</p>
        <ul class="contact-list">
          <li>
            <svg viewBox="0 0 16 16" aria-hidden="true"><path d="M2 6c0-2 2.5-3.5 6-3.5S14 4 14 6v1.2h-3V5.8H5v1.4H2z M4 8h8l1.5 5.5h-11z"/></svg>
            (555) 214-3907
          </li>
          <li>
            <svg viewBox="0 0 16 16" aria-hidden="true"><path d="M1 3h14v10H1z M2.2 4.2 8 8.6l5.8-4.4z" fill-rule="evenodd"/></svg>
            sales@738kv.com
          </li>
          <li>
            <svg viewBox="0 0 16 16" aria-hidden="true"><path d="M6.5 9.5l3-3 M5 7.5 3 9.5a2.1 2.1 0 0 0 3 3l2-2 M11 8.5l2-2a2.1 2.1 0 0 0-3-3l-2 2" stroke="currentColor" stroke-width="1.8" fill="none" stroke-linecap="round"/></svg>
            www.738kv.com
          </li>
          <li>
            <svg viewBox="0 0 16 16" aria-hidden="true"><circle cx="8" cy="8" r="6.5"/></svg>
            @738KV
          </li>
        </ul>
      </div>
    </div>
    <div class="base-band"></div>
  </section>
</main>
</body>
</html>
```